Inspiration Poster

Inspirational Poster that has a Kamran Dulo like abstract look (http://www.vexalo.com/images/search?q=kamran+dulo&FORM=HDRSC2) with the text:

"we walk not in order to arrive at the promise land but because walking itself is a revolution"
-Peter Ambrick

```html
<!DOCTYPE html>
<html lang="en">
<head>
<meta charset="utf-8">
<title>Inspiration Poster</title>
<link rel="stylesheet" href="https://fonts.googleapis.com/css2?family=Stint+Ultra+Condensed&display=swap">
<style>
  :root {
    --paper: #ffffff;
    --wash-top: #e86ee8;
    --wash-mid: #c43fe0;
    --wash-low: #9a4fd8;
    --wash-bottom: #8a2fd6;
    --ink-light: #ffffff;
    --ink-credit: #7a2fb0;
    --tab-notch: #6a2a9a;
  }
  html, body {
    margin: 0;
    padding: 0;
    overflow: hidden;
  }
  .poster {
    position: relative;
    width: 849px;
    height: 1200px;
    background: var(--paper);
    overflow: hidden;
    font-family: "Stint Ultra Condensed", serif;
  }
  .paint-wash {
    position: absolute;
    left: 56px;
    top: 30px;
    width: 744px;
    height: 1135px;
    background:
      radial-gradient(ellipse at 30% 20%, rgba(255,160,240,0.45), transparent 55%),
      radial-gradient(ellipse at 60% 70%, rgba(150,120,230,0.4), transparent 50%),
      linear-gradient(180deg, var(--wash-top) 0%, var(--wash-mid) 45%, var(--wash-low) 70%, var(--wash-bottom) 100%);
    border-radius: 6px 10px 4px 8px;
    filter: blur(0.6px);
  }
  .quote {
    position: absolute;
    left: 0;
    top: 140px;
    width: 849px;
    margin: 0;
    text-align: center;
    color: var(--ink-light);
    font-size: 98px;
    line-height: 117px;
    letter-spacing: 3px;
    font-weight: 400;
  }
  .quote span {
    display: block;
  }
  .credit-tab {
    position: absolute;
    left: 418px;
    top: 1083px;
    width: 352px;
    height: 45px;
    background: var(--paper);
  }
  .credit-notch {
    position: absolute;
    left: 418px;
    top: 1083px;
  }
  .credit {
    position: absolute;
    left: 418px;
    top: 1083px;
    width: 352px;
    height: 45px;
    line-height: 45px;
    text-align: center;
    color: var(--ink-credit);
    font-size: 22px;
    letter-spacing: 1.5px;
    margin: 0;
  }
</style>
</head>
<body>
  <main class="poster">
    <div class="paint-wash" role="img" aria-label="Abstract watercolour wash in pink and violet with rough brushed edges"></div>

    <blockquote class="quote">
      <span>“we walk</span>
      <span>not in order</span>
      <span>to arrive</span>
      <span>at the</span>
      <span>promise land</span>
      <span>but because walking</span>
      <span>itself is a</span>
      <span>revolution”</span>
    </blockquote>

    <div class="credit-tab"></div>
    <svg class="credit-notch" width="40" height="20" viewBox="0 0 40 20" aria-hidden="true">
      <polygon points="0,0 40,14 0,14" fill="var(--tab-notch)" opacity="0.55"/>
    </svg>
    <p class="credit">-Peter Ambrick</p>
  </main>
</body>
</html>
```